Join Wait / Reservations Handout

This is a handout for guests with information about the ability to join our
waitlist and/or make reservations. It will be handed out to any guest that ends up waiting on our waitlist to be seated. It will describe how our waitlist and reservations system works. It is informational for them to download our mobile app.

It was forcing me to move the look and feel sliders. Please refer to our branding guide for look and feel.

Industry/Entity Type

Hospitality

Contact Information for Business Card

One of the attached documents give a very generic layout of the information we need on this card. This layout is more for where we wanted the information placed and has nothing to do with the design aspects of the piece. Please use your imagination. Any of the 5 colors in the branding guide can be used anywhere. The pineapple design can be used anywhere in any color combination.

If you require any other files please let me know. Thanks

Other font styles liked:
• Please see attached branding guide

Requirements
Must have
• The only color requirement is that the logo be the blue with teal lettering...This has to match our app store logo.

```html
<!DOCTYPE html>
<html lang="en">
<head>
<meta charset="utf-8">
<title>Join Wait / Reservations Handout</title>
<link href="https://fonts.googleapis.com/css2?family=Cinzel:wght@400;700;900&display=swap" rel="stylesheet">
<style>
  :root {
    --teal: #66adb3;
    --teal-deep: #4f969c;
    --navy: #0f3a4e;
    --paper: #ffffff;
    --mist: #ececec;
    --stage: #e3e3e6;
    --dots: #2c5866;
  }
  * { box-sizing: border-box; margin: 0; padding: 0; }
  html, body { width: 1145px; height: 1200px; overflow: hidden; }
  body {
    background: var(--stage);
    font-family: "Cinzel", "Times New Roman", serif;
    position: relative;
  }
  .card {
    position: absolute;
    top: 162px;
    width: 500px;
    height: 877px;
    overflow: hidden;
    box-shadow: 0 10px 28px rgba(0,0,0,.22);
  }
  .card--front { left: 50px; }
  .card--back { left: 595px; background: var(--mist); }

  /* front */
  .front-pattern {
    position: absolute; inset: 0;
    background: linear-gradient(160deg, var(--teal) 0%, var(--teal-deep) 100%);
  }
  .tag {
    position: absolute;
    background: var(--paper);
    color: var(--navy);
    box-shadow: 0 6px 14px rgba(0,0,0,.3);
    text-align: center;
    line-height: 1.15;
  }
  .tag--top {
    top: 10px; left: 100px; width: 420px; height: 130px;
    transform: rotate(-14deg);
    font-size: 25px; padding-top: 38px; padding-right: 30px;
  }
  .tag--bottom {
    bottom: -30px; left: -40px; width: 440px; height: 150px;
    transform: rotate(-14deg);
    font-size: 25px; padding: 22px 40px 0 140px; text-align: right;
  }
  .store-note {
    position: absolute; left: 12px; bottom: 18px;
    font-size: 13px; font-weight: 700; color: #8a9a50;
  }
  .brand-seal {
    position: absolute; left: 80px; top: 270px;
    width: 340px; height: 340px; border-radius: 50%;
    background: var(--paper);
    box-shadow: 0 8px 20px rgba(0,0,0,.3);
    display: flex; align-items: center; justify-content: center;
  }
  .brand-seal::before {
    content: ""; position: absolute; inset: 14px;
    border: 2px solid var(--navy); border-radius: 50%;
  }
  .brand-name { color: var(--navy); font-weight: 700; font-size: 36px; letter-spacing: 1px; }

  /* back */
  .band {
    position: absolute; left: -30px; width: 560px;
    box-shadow: 0 6px 12px rgba(0,0,0,.25);
  }
  .band--teal { background: var(--teal); color: var(--paper); }
  .band--paper { background: var(--mist); color: var(--teal); }
  .band--paper::after {
    content: ""; position: absolute; inset: 8px 36px;
    border: 2px dotted var(--dots); pointer-events: none;
  }
  .band--join { top: -30px; height: 262px; transform: rotate(-2.5deg); }
  .band--reserve { top: 222px; height: 232px; transform: rotate(1.5deg); }
  .band--buffet { top: 448px; height: 228px; transform: rotate(-2deg); }
  .band--groups { top: 664px; height: 240px; transform: rotate(0.8deg); }

  .join-title { position: absolute; left: 70px; top: 100px; font-size: 40px; font-weight: 700; line-height: 1.1; }
  .join-mark { position: absolute; right: 60px; top: 90px; text-align: center; font-weight: 700; }
  .join-mark .brand-name { color: var(--paper); font-size: 24px; display: block; }
  .join-mark small { font-size: 20px; display: block; margin-top: 16px; }

  .reserve-icon { position: absolute; left: 86px; top: 26px; width: 140px; }
  .reserve-icon span { display: block; text-align: center; font-weight: 700; font-size: 19px; margin-top: 4px; }
  .reserve-text { position: absolute; left: 250px; top: 28px; width: 250px; text-align: center; font-weight: 700; }
  .reserve-text h2 { font-size: 40px; line-height: 1.1; }
  .reserve-text p { font-size: 15px; line-height: 1.15; margin-top: 4px; }

  .buffet { position: absolute; left: 40px; right: 40px; top: 40px; text-align: center; font-weight: 700; }
  .buffet .lead { font-size: 36px; }
  .buffet .big { font-size: 70px; font-weight: 900; line-height: 1; }
  .buffet .note { font-size: 21px; margin-top: 26px; }

  .groups { position: absolute; left: 40px; right: 40px; top: 40px; text-align: center; font-weight: 700; line-height: 1; }
  .groups .lead { font-size: 38px; }
  .groups .big { font-size: 52px; font-weight: 900; }
  .groups .note { font-size: 20px; margin-top: 20px; }
</style>
</head>
<body>

<section class="card card--front">
  <div class="front-pattern" role="img" aria-label="Decorative teal geometric pattern background"></div>
  <div class="tag tag--top">Save the Wait…<br>…Download our App</div>
  <div class="brand-seal"><span class="brand-name">Harborline</span></div>
  <div class="tag tag--bottom">Search<br>“Harborline<br>Eastfield”</div>
  <span class="store-note">Mobile App</span>
</section>

<section class="card card--back">
  <div class="band band--paper band--groups">
    <div class="groups">
      <div class="lead">Large Groups</div>
      <div class="big">Handled</div>
      <div class="note">Contacted by Catering Manager</div>
    </div>
  </div>

  <div class="band band--teal band--buffet">
    <div class="buffet">
      <div class="lead">Sunday + Holiday</div>
      <div class="big">Buffets</div>
      <div class="note">(Coming June 2018)</div>
    </div>
  </div>

  <div class="band band--paper band--reserve">
    <div class="reserve-icon">
      <svg viewBox="0 0 140 120" width="140" height="120" aria-hidden="true">
        <rect x="6" y="18" width="104" height="86" rx="10" fill="none" stroke="#66adb3" stroke-width="8"/>
        <rect x="6" y="18" width="104" height="22" rx="8" fill="#66adb3"/>
        <rect x="26" y="6" width="8" height="22" rx="3" fill="#66adb3"/>
        <rect x="82" y="6" width="8" height="22" rx="3" fill="#66adb3"/>
        <g fill="#66adb3">
          <rect x="20" y="50" width="18" height="14"/><rect x="44" y="50" width="18" height="14"/><rect x="68" y="50" width="18" height="14"/>
          <rect x="20" y="70" width="18" height="14"/><rect x="44" y="70" width="18" height="14"/>
        </g>
        <circle cx="104" cy="90" r="28" fill="#ececec" stroke="#66adb3" stroke-width="8"/>
        <path d="M104 74 V92 H118" fill="none" stroke="#66adb3" stroke-width="6" stroke-linecap="round"/>
      </svg>
      <span>Anytime</span>
    </div>
    <div class="reserve-text">
      <h2>When to<br>Reserve?</h2>
      <p>2 hours in advance<br>(excluding weekend,<br>open – 2pm)</p>
    </div>
  </div>

  <div class="band band--teal band--join">
    <h2 class="join-title">When to<br>Join Wait?</h2>
    <div class="join-mark">
      <span class="brand-name">Harborline</span>
      <small>Anytime</small>
    </div>
  </div>
</section>

</body>
</html>
```